Velmora Swinger site - new website, blogsite and merchandise point, connection to torvenix

We are a well established Swingers Club in the North east of UK and already have an existing site. www.velmora.co.uk, BUT we have changed our logo and our information on the site needs to be updated.

We are changing our hosting site to Nimbrastack.com ,also wanting to start a blog which is linked to the club, plus we wish to sell a small exclusive range of Velmora linked merchandise which will also be available on Torvenix.

I have attached a pdf of the majority of the content. additionally we will provide pictures and a videoclip which should be able to be viewed by pc's, lap tops and mobile phones (the whole website must be fully accessible via phone).

The new site must be able to be updated by someone with medium computer knowledge (usually me), by no means expert. Updates will generally be new pictures and written information. The site must be able to be transferred to NimbraStack.

Velmora is one of the countries leading clubs and emphasises friendliness, fun & safety for its members, we look after you to ensure your experience is the best we can offer. We are very proud of our reputation, built up over more than 10 years.

Target Market(s)

Swingers, dreamers & fantasists, alternative lifestyle people

Coding

Coded - Design and coding required

Number of Pages Required

5+ page

Font styles to use
Sans Serif

Colors
000000
ec1f27
fbfbfb
eeeeee
eaeaea

Requirements
Must have
• website with blog attached, link to torvenix & quidlane, ability to run videoclip and picture album and must be compatable to transfer easily to Nimbrastack and be updated by non-professional (who can learn)
• Straightforward & easy to navigate
• over 18 content page with enter button
Nice to have
• sexy site
• link to chirpet maybe
• black site would be nice with red or white writing
Should not have
• children and animals in anyway shape or form

```html
<!DOCTYPE html>
<html lang="en">
<head>
<meta charset="utf-8">
<title>Velmora – Swingers Club</title>
<link rel="stylesheet" href="https://fonts.googleapis.com/css2?family=Bree+Serif&family=Poppins:wght@400;500;600&display=swap">
<style>
:root{
  --black:#000000;
  --header:#17110f;
  --red:#ec1f27;
  --red-dark:#c8101a;
  --white:#fbfbfb;
  --light:#eeeeee;
  --card:#141414;
  --gold:#f5c33b;
}
*{margin:0;padding:0;box-sizing:border-box}
html,body{width:1200px;height:2889px;overflow:hidden;background:var(--black)}
body{position:relative;font-family:'Poppins',sans-serif;color:var(--white)}
.heading{font-family:'Bree Serif',serif;font-weight:400}
.abs{position:absolute}

.site-header{left:0;top:0;width:1200px;height:79px;background:var(--header);display:flex;align-items:center;justify-content:center}
.brand{font-family:'Bree Serif',serif;font-size:44px;letter-spacing:4px;color:var(--white);display:flex;align-items:center;gap:8px}
.brand-dot{width:8px;height:8px;background:var(--red);border-radius:50%;margin-top:-24px}

.main-nav{left:0;top:79px;width:1200px;height:35px;background:var(--red);display:flex;justify-content:space-around;align-items:center;padding:0 70px}
.main-nav a{color:var(--white);font-size:13px;text-decoration:none}

.hero{left:0;top:114px;width:1200px;height:466px;background:linear-gradient(180deg,#4a2a28 0%,#3a2624 45%,#2c2220 100%)}
.hero-title{left:0;top:260px;width:1200px;text-align:center;font-size:37px;line-height:80px;color:var(--white);letter-spacing:.5px}
.hero-btn{left:480px;top:406px;width:248px;height:47px;background:var(--red-dark);color:var(--white);font-family:'Bree Serif',serif;font-size:25px;display:flex;align-items:center;justify-content:center}
.hero-dots{left:585px;top:543px;display:flex;gap:4px}
.hero-dots span{width:10px;height:10px;border:2px solid var(--white);border-radius:50%}

.section-title{left:0;width:1200px;text-align:center;font-size:26px;color:var(--white)}
.section-text{text-align:center;font-size:10.4px;line-height:21px;color:var(--light)}
.section-text strong{font-weight:600}

.feature{width:273px;height:220px;background:var(--card);padding:0 24px}
.feature-head{height:114px;display:flex;align-items:center;justify-content:center;gap:12px;white-space:nowrap}
.feature-head svg{width:40px;height:40px;flex:none}
.feature-name{font-family:'Bree Serif',serif;font-size:22px;line-height:29px;color:var(--white)}
.feature-text{text-align:center;font-size:10.4px;line-height:20px;color:var(--light)}

.member-banner{left:0;top:1527px;width:1200px;height:256px;background:linear-gradient(120deg,#2e2e2e,#1a1a1a 60%,#3a3a3a)}
.member-photo{left:0;top:1527px;width:664px;height:256px;background:linear-gradient(135deg,#3a2c24,#241c18 60%,#4a3a30)}
.member-panel{left:664px;top:1527px;width:370px;height:256px;text-align:center}
.member-brand{position:absolute;left:0;top:14px;width:370px;font-family:'Bree Serif',serif;font-size:30px;letter-spacing:3px}
.member-cta{position:absolute;left:0;top:79px;width:370px;font-size:21px}
.member-offer{position:absolute;left:0;top:119px;width:370px;font-size:15px;line-height:24px;color:var(--red);font-weight:500}
.member-rule{position:absolute;left:14px;top:143px;width:345px;height:1px;background:var(--white)}
.buy-btn{position:absolute;left:96px;top:181px;width:177px;height:46px;background:var(--gold);border-radius:4px;color:#111;font-size:17px;font-weight:500;display:flex;align-items:center;justify-content:center}

.blog-card{width:310px;height:414px;background:var(--card)}
.blog-img{width:310px;height:230px}
.blog-text{padding:16px 20px;text-align:center;font-size:10.4px;line-height:21px;color:var(--light)}

.diamond{width:177px;height:177px;transform:rotate(45deg)}
.price{left:499px;top:2643px;width:200px;text-align:center}
.price-amount{font-size:30px;font-weight:600;line-height:40px}
.price-amount small{font-size:15px;font-weight:400}
.price-label{font-size:17px;line-height:24px}

.site-footer{left:0;top:2831px;width:1200px;height:58px;background:var(--red);display:flex;align-items:center;justify-content:center;font-size:12px;font-weight:500}
</style>
</head>
<body>

<header class="abs site-header">
  <div class="brand">VELMORA<span class="brand-dot"></span></div>
</header>

<nav class="abs main-nav">
  <a href="#">Home</a><a href="#">Diary</a><a href="#">Theme Parties</a><a href="#">TV/TG and Admirers</a><a href="#">Membership</a><a href="#">FAQs</a><a href="#">Rooms</a><a href="#">Contact US</a><a href="#">Links</a>
</nav>

<section class="abs hero" role="img" aria-label="Photo of a warmly lit club bedroom with patterned wallpaper, bed and armchairs"></section>
<h1 class="abs heading hero-title">A true Swingers Club Where You Can Meet,<br>Socialise And Play (if you want.......)</h1>
<a class="abs hero-btn">Call Us Today</a>
<div class="abs hero-dots"><span></span><span></span><span></span></div>

<h2 class="abs heading section-title" style="top:624px">A Great Place To Meet And Play!</h2>
<p class="abs section-text" style="left:160px;top:674px;width:880px">Velmora was established in Harrowby in 2004 by Martin (now retired) and has been at this location in Fernshire and run by Carol since 2008. During this time we have upgraded and improved the club beyond recognition. We have a varied group of all sorts of people that work here and help here and because of this we can understand most fetishes and sexual orientations, all the people that help and work here do so because they love this environment <strong>Read More</strong></p>

<div class="abs feature" style="left:166px;top:772px">
  <div class="feature-head">
    <svg viewBox="0 0 44 44" fill="#ec1f27"><rect x="4" y="20" width="32" height="12" rx="3"/><rect x="8" y="32" width="4" height="5"/><rect x="28" y="32" width="4" height="5"/><path d="M8 20V9a4 4 0 0 1 8 0v2h-3V9a1 1 0 0 0-2 0v11z"/><circle cx="22" cy="14" r="2"/><circle cx="28" cy="12" r="2"/></svg>
    <span class="feature-name">Hot Tub</span>
  </div>
  <p class="feature-text">Lorem Ipsum is simply dummy text of the printing and typesetting industry. Lorem Ipsum has been the industry's standard dummy text ever since the 1500s</p>
</div>
<div class="abs feature" style="left:466px;top:772px">
  <div class="feature-head">
    <svg viewBox="0 0 44 44" fill="none" stroke="#ec1f27" stroke-width="4"><rect x="6" y="6" width="32" height="32"/><path d="M22 6v32M6 22h32"/></svg>
    <span class="feature-name">Steam Room</span>
  </div>
  <p class="feature-text">Lorem Ipsum is simply dummy text of the printing and typesetting industry. Lorem Ipsum has been the industry's standard dummy text ever since the 1500s</p>
</div>
<div class="abs feature" style="left:765px;top:772px">
  <div class="feature-head">
    <svg viewBox="0 0 44 44" fill="#ec1f27"><rect x="4" y="10" width="36" height="10" rx="2"/><rect x="9" y="13" width="10" height="5" fill="#141414"/><rect x="25" y="13" width="10" height="5" fill="#141414"/><rect x="2" y="21" width="40" height="12" rx="2"/><rect x="4" y="33" width="4" height="4"/><rect x="36" y="33" width="4" height="4"/></svg>
    <span class="feature-name">Dark Room</span>
  </div>
  <p class="feature-text">Lorem Ipsum is simply dummy text of the printing and typesetting industry. Lorem Ipsum has been the industry's standard dummy text ever since the 1500s</p>
</div>

<div class="abs feature" style="left:166px;top:1015px">
  <div class="feature-head">
    <svg viewBox="0 0 44 44" fill="#ec1f27"><circle cx="22" cy="12" r="5"/><path d="M14 30c0-6 4-11 8-11s8 5 8 11z"/><rect x="4" y="30" width="36" height="4"/><rect x="8" y="34" width="3" height="6"/><rect x="33" y="34" width="3" height="6"/><path d="M6 8q3 4 0 8q3 4 0 8" fill="none" stroke="#ec1f27" stroke-width="2"/><path d="M38 8q3 4 0 8q3 4 0 8" fill="none" stroke="#ec1f27" stroke-width="2"/></svg>
    <span class="feature-name">Sauna</span>
  </div>
  <p class="feature-text">Lorem Ipsum is simply dummy text of the printing and typesetting industry. Lorem Ipsum has been the industry's standard dummy text ever since the 1500s</p>
</div>
<div class="abs feature" style="left:466px;top:1015px">
  <div class="feature-head">
    <svg viewBox="0 0 44 44" fill="none" stroke="#ec1f27" stroke-width="3"><path d="M12 14h20c6 0 9 8 9 15 0 5-4 6-7 3l-4-4H14l-4 4c-3 3-7 2-7-3 0-7 3-15 9-15z"/><path d="M12 19v6M9 22h6"/><circle cx="30" cy="20" r="1.5" fill="#ec1f27"/><circle cx="33" cy="24" r="1.5" fill="#ec1f27"/></svg>
    <span class="feature-name">Private<br>Playrooms</span>
  </div>
  <p class="feature-text">Lorem Ipsum is simply dummy text of the printing and typesetting industry. Lorem Ipsum has been the industry's standard dummy text ever since the 1500s</p>
</div>
<div class="abs feature" style="left:765px;top:1015px">
  <div class="feature-head">
    <svg viewBox="0 0 44 44" fill="none" stroke="#ec1f27" stroke-width="3"><path d="M4 6v32M40 20v18M4 28h36M4 20h36"/><rect x="8" y="13" width="8" height="6" rx="2"/></svg>
    <span class="feature-name">Rays Dungeon</span>
  </div>
  <p class="feature-text">Lorem Ipsum is simply dummy text of the printing and typesetting industry. Lorem Ipsum has been the industry's standard dummy text ever since the 1500s</p>
</div>

<div class="abs feature" style="left:327px;top:1262px">
  <div class="feature-head">
    <svg viewBox="0 0 44 44" fill="#ec1f27"><circle cx="22" cy="12" r="6"/><circle cx="10" cy="16" r="5"/><circle cx="34" cy="16" r="5"/><path d="M12 38c0-10 4-16 10-16s10 6 10 16z"/><path d="M2 36c0-8 3-12 8-12 2 0 3 1 4 2-2 3-3 6-3 10z"/><path d="M42 36c0-8-3-12-8-12-2 0-3 1-4 2 2 3 3 6 3 10z"/></svg>
    <span class="feature-name">Group Rooms</span>
  </div>
  <p class="feature-text">Lorem Ipsum is simply dummy text of the printing and typesetting industry. Lorem Ipsum has been the industry's standard dummy text ever since the 1500s</p>
</div>
<div class="abs feature" style="left:628px;top:1262px">
  <div class="feature-head">
    <svg viewBox="0 0 44 44" fill="#ec1f27"><path d="M10 4h6v36h-6z"/><path d="M16 4l16 5v30l-16 1z"/></svg>
    <span class="feature-name">Amsterdam Room</span>
  </div>
  <p class="feature-text">Lorem Ipsum is simply dummy text of the printing and typesetting industry. Lorem Ipsum has been the industry's standard dummy text ever since the 1500s</p>
</div>

<section class="abs member-banner"></section>
<div class="abs member-photo" role="img" aria-label="Photo of a lounge with a sofa and a black tiled fireplace"></div>
<div class="abs member-panel">
  <div class="member-brand">VELMORA</div>
  <div class="member-cta">Get Our Membership</div>
  <div class="member-offer">Never Before<br>Grab The Offer Now</div>
  <div class="member-rule"></div>
  <div class="buy-btn">Buy From Torvenix</div>
</div>

<h2 class="abs heading section-title" style="top:1822px">From Our Blog</h2>
<p class="abs section-text" style="left:140px;top:1872px;width:920px">Lorem Ipsum is simply dummy text of the printing and typesetting industry. Lorem Ipsum has been the industry's standard dummy text ever since the 1500sLorem Ipsum is simply dummy text of the printing and typesetting industry. Lorem Ipsum has been the industry's standard dummy text ever since the 1500sLorem</p>

<article class="abs blog-card" style="left:94px;top:1951px">
  <div class="blog-img" role="img" aria-label="Photo of an attic bedroom with patterned wallpaper and a lamp" style="background:linear-gradient(135deg,#6a5a52,#3a2e2a)"></div>
  <p class="blog-text">Lorem Ipsum is simply dummy text of the printing and typesetting industry. Lorem Ipsum has been the industry's standard dummy text ever since the 1500sLorem Ipsum is simply dummy text of the printing and typesetting industry. Lorem Ipsum has been the industry's standard dummy text ever since the 1500s</p>
</article>
<article class="abs blog-card" style="left:441px;top:1951px">
  <div class="blog-img" role="img" aria-label="Photo of a red-lit bedroom with red bedding" style="background:linear-gradient(135deg,#8a3a22,#5a1a12)"></div>
  <p class="blog-text">Lorem Ipsum is simply dummy text of the printing and typesetting industry. Lorem Ipsum has been the industry's standard dummy text ever since the 1500sLorem Ipsum is simply dummy text of the printing and typesetting industry. Lorem Ipsum has been the industry's standard dummy text ever since the 1500s</p>
</article>
<article class="abs blog-card" style="left:784px;top:1951px">
  <div class="blog-img" role="img" aria-label="Photo of a bright bedroom with white bedding and a city print" style="background:linear-gradient(135deg,#b8a890,#7a6a58)"></div>
  <p class="blog-text">Lorem Ipsum is simply dummy text of the printing and typesetting industry. Lorem Ipsum has been the industry's standard dummy text ever since the 1500sLorem Ipsum is simply dummy text of the printing and typesetting industry. Lorem Ipsum has been the industry's standard dummy text ever since the 1500s</p>
</article>

<h2 class="abs heading section-title" style="top:2398px">Velmora Membership</h2>
<p class="abs section-text" style="left:146px;top:2446px;width:908px">Sometimes we put new memberships on hold for certain categories, this is a private member's club and if we restrict membership it's for good reason, mainly to keep the balance right. If you already know a member then ask them to introduce you, (ask them to call or write so your name is on the guest list) or phone on the Velmora phone to arrange your first visit. The club phone is switched on from 2pm on the days we open (Wed/Fri/Sat).</p>

<div class="abs diamond" style="left:214px;top:2584px;background:linear-gradient(135deg,#8a6a58,#4a3a32)" role="img" aria-label="Photo of a smiling couple"></div>
<div class="abs diamond" style="left:511px;top:2584px;background:linear-gradient(135deg,#e0303a,#b81820)" role="img" aria-label="Photo of a single guy tinted red"></div>
<div class="abs diamond" style="left:808px;top:2584px;background:linear-gradient(135deg,#9a7a68,#3a2a24)" role="img" aria-label="Photo of a single woman"></div>
<div class="abs price">
  <div class="price-amount">£30.00 <small>per</small></div>
  <div class="price-label">Single Guy</div>
</div>

<footer class="abs site-footer">copyright © 2017 Velmora. All Rights Reserved. Privacy Policy.</footer>

</body>
</html>
```